Label design for one hand cream.

The name of the company is Luvo. We are launching a hand cream that is also an immediate cleaner without any water. It removes dirt from your hands without using water. After the use, your hands will be soft. It could be used in your feet too.

The company logo reminds of plants, nature and we would like this approach too. Please, remove the words "Produtos Naturais" from the logo.

Target Market(s)

Public in General. Mostly women.

Industry/Entity Type

Cosmetics

Font styles to use
Sans Serif

Colors
33b8a4
00a990
9bcb3c
acd036
fee087
fece3e
ffc214
fbed22
fbee3e

Requirements
Must have
• You must use the words in the label. Please, see the file attached but just use the WORDS, not the same structure. The image must be 15,5cm high and 7,5 cm wide.
• Use a darker green and some GOLDEN lines or details. You can even put the Logo plant on the golden color.
• "Frisson Duo"
• "Ação 3 em 1: Esfoliante, limpeza e hidratação"
• "Regeneração Celular"
• "Velvet Tending"
• Logo of the company "Luvo" (attached).
• Please, REMOVE the words "Produtos Naturais" from the logo.
• Elegance and show softness.
• Something that reminds of nature or fresh.
Should not have
• Strong colors or many images that distract the information.

```html
<!DOCTYPE html>
<html lang="pt">
<head>
<meta charset="UTF-8">
<title>Luvo — Frisson Duo label</title>
<link rel="stylesheet" href="https://fonts.googleapis.com/css2?family=Quicksand:wght@700&family=Roboto+Condensed:ital,wght@1,400&family=Mulish:wght@400&display=swap">
<style>
  :root {
    --page-bg: #ebebeb;
    --label-green: #0f5f10;
    --mark-green: #1c6b1d;
    --brand-green: #93cd74;
    --gold-light: #f3df7a;
    --gold-deep: #c9a22c;
    --text-white: #ffffff;
    --text-dark: #3a3f44;
    --chip-one: #e6e9ec;
    --chip-two: #c9dfe6;
    --chip-three: #a8d5c7;
  }
  * { margin: 0; padding: 0; box-sizing: border-box; }
  html, body {
    width: 1200px;
    height: 800px;
    overflow: hidden;
    background: var(--page-bg);
  }
  .label {
    position: absolute;
    left: 360px;
    top: 20px;
    width: 480px;
    height: 760px;
    background: var(--label-green);
    overflow: hidden;
  }
  .label__mark {
    position: absolute;
    left: -200px;
    top: 265px;
    width: 470px;
    height: 470px;
    border-radius: 50%;
    background: var(--mark-green);
  }
  .brand {
    position: absolute;
    right: 39px;
    top: 80px;
    display: flex;
    align-items: center;
    gap: 18px;
  }
  .brand__dot {
    width: 58px;
    height: 58px;
    border-radius: 50%;
    background: linear-gradient(135deg, var(--gold-light), var(--gold-deep));
  }
  .brand__name {
    font-family: "Quicksand", sans-serif;
    font-weight: 700;
    font-size: 128px;
    line-height: 1;
    color: var(--brand-green);
    letter-spacing: -2px;
  }
  .product-name {
    position: absolute;
    right: 39px;
    top: 280px;
    font-family: "Roboto Condensed", sans-serif;
    font-style: italic;
    font-weight: 400;
    font-size: 52px;
    line-height: 1.2;
    background: linear-gradient(180deg, var(--gold-light), var(--gold-deep));
    -webkit-background-clip: text;
    background-clip: text;
    color: transparent;
  }
  .action-title {
    position: absolute;
    right: 39px;
    top: 380px;
    font-family: "Mulish", sans-serif;
    font-size: 33px;
    line-height: 1.2;
    color: var(--text-white);
  }
  .action-bar {
    position: absolute;
    left: 30px;
    top: 434px;
    width: 411px;
    height: 51px;
    display: flex;
    font-family: "Mulish", sans-serif;
    font-size: 27px;
    color: var(--text-dark);
  }
  .action-bar__item {
    display: flex;
    align-items: center;
    justify-content: center;
  }
  .action-bar__item--scrub { width: 143px; background: var(--chip-one); }
  .action-bar__item--clean { width: 126px; background: var(--chip-two); }
  .action-bar__item--hydrate { width: 142px; background: var(--chip-three); }
  .benefits {
    position: absolute;
    right: 39px;
    top: 598px;
    text-align: right;
    font-family: "Mulish", sans-serif;
    font-size: 24px;
    line-height: 1.22;
    color: var(--text-white);
  }
</style>
</head>
<body>
  <main class="label">
    <div class="label__mark" role="img" aria-label="Faint brand plant emblem"></div>

    <div class="brand">
      <span class="brand__dot"></span>
      <span class="brand__name">Luvo</span>
    </div>

    <h1 class="product-name">Frisson Duo</h1>

    <p class="action-title">Ação 3 em 1</p>
    <div class="action-bar">
      <span class="action-bar__item action-bar__item--scrub">Esfoliante</span>
      <span class="action-bar__item action-bar__item--clean">limpeza</span>
      <span class="action-bar__item action-bar__item--hydrate">hidratação</span>
    </div>

    <p class="benefits">Regeneração Celular<br>Velvet Tending</p>
  </main>
</body>
</html>
```